Wine Label Designs

Three wine labels are required for a White, a Rose and a Red Wine in a range.

The range is going to be called Silverfen and should have a heraldic / Arthurian essence but in a contemporary style.

The three wines are proposed as:
1. Hour of Lanterns - white wine
The story here is that a dragon-shaped comet is seen in the night skies and this heralded the Hour of Lanterns and the coming of King Arthur.

2. Hour of Blossoming - rose wine
This is about young love, romance, with styling compatible with the Hour of Lanterns.

3. Hour of Iron - red wine
Here we have the coming of age and learning to overcome adversity in heroic style. Again, styling to be compatible with the Hour of Lanterns/Blossoming.

Target Market(s)

Millennials and young professionals

Font styles to use
Decorative
Script

Colors

Designer to choose colors to be used in the design.

Requirements
Must have
• Range Name
• Image appropriate to each wine title
• Wine Name
• Each label needs to be unique
Nice to have
• One item that can be foiled on each label
Should not have
• Cluttered imagery
• Designs too similar to each other

```html
<!DOCTYPE html>
<html lang="en">
<head>
<meta charset="utf-8">
<title>Hour of Lanterns – White Wine Label</title>
<link rel="stylesheet" href="https://fonts.googleapis.com/css2?family=Uncial+Antiqua&family=UnifrakturMaguntia&display=swap">
<style>
  :root {
    --backdrop: #e7e6e0;
    --paper: #ffffff;
    --ink: #141414;
    --gold-light: #efe2c2;
    --gold: #c9ab72;
    --gold-deep: #a88a52;
    --night: #0b0b0b;
    --night-soft: #262626;
    --haze: #4a4a4a;
  }
  * { box-sizing: border-box; margin: 0; padding: 0; }
  html, body {
    width: 1197px;
    height: 1200px;
    overflow: hidden;
    background: var(--backdrop);
  }
  .label {
    position: absolute;
    left: 318px;
    top: 145px;
    width: 560px;
    height: 910px;
    color: var(--ink);
    font-family: "Uncial Antiqua", serif;
  }
  .label__shape {
    position: absolute;
    inset: 0;
    width: 560px;
    height: 910px;
  }
  .title {
    position: absolute;
    left: 0;
    width: 100%;
    text-align: center;
    line-height: 1;
  }
  .title--top { top: 58px; font-size: 62px; }
  .title--joiner { top: 140px; font-size: 30px; }
  .title--bottom { top: 176px; font-size: 60px; }
  .title-rule {
    position: absolute;
    top: 148px;
    left: 80px;
    width: 400px;
    height: 20px;
  }
  .knot-frame {
    position: absolute;
    left: 58px;
    top: 262px;
    width: 444px;
    height: 344px;
    background:
      radial-gradient(ellipse 56% 72% at 50% 50%, transparent 0 66%, rgba(201,171,114,0.55) 74%, rgba(168,138,82,0.75) 100%);
    -webkit-mask: linear-gradient(#000 0 0);
    border-radius: 6px;
  }
  .emblem {
    position: absolute;
    left: 108px;
    top: 258px;
    width: 344px;
    height: 344px;
    border-radius: 50%;
    background:
      radial-gradient(ellipse 70% 22% at 50% 92%, var(--haze), transparent 70%),
      radial-gradient(ellipse 40% 18% at 40% 48%, rgba(255,255,255,0.22), transparent 70%),
      radial-gradient(circle at 50% 45%, var(--night-soft), var(--night) 75%);
  }
  .emblem__caption {
    position: absolute;
    left: 108px;
    top: 290px;
    width: 344px;
    text-align: center;
    font-family: "UnifrakturMaguntia", serif;
    font-size: 24px;
    color: var(--paper);
  }
  .spec {
    position: absolute;
    top: 640px;
    font-size: 28px;
    line-height: 1;
  }
  .spec--abv { left: 74px; }
  .spec--volume { right: 74px; }
</style>
</head>
<body>
  <main class="label" aria-label="Hour of Lanterns white wine label">
    <svg class="label__shape" viewBox="0 0 560 910" aria-hidden="true">
      <defs>
        <linearGradient id="gold-frame" x1="0" y1="0" x2="1" y2="1">
          <stop offset="0" stop-color="#a88a52"/>
          <stop offset="0.5" stop-color="#e9d8ae"/>
          <stop offset="1" stop-color="#b59762"/>
        </linearGradient>
      </defs>
      <polygon points="0,0 560,0 560,910 280,640 0,910" fill="var(--paper)"/>
      <polygon points="20,22 540,22 540,868 280,622 20,868" fill="none" stroke="url(#gold-frame)" stroke-width="6"/>
    </svg>

    <h1 class="title title--top">Hour</h1>
    <svg class="title-rule" viewBox="0 0 400 20" aria-hidden="true">
      <line x1="6" y1="10" x2="150" y2="10" stroke="var(--ink)" stroke-width="3"/>
      <line x1="250" y1="10" x2="394" y2="10" stroke="var(--ink)" stroke-width="3"/>
      <line x1="4" y1="2" x2="4" y2="18" stroke="var(--ink)" stroke-width="4"/>
      <line x1="396" y1="2" x2="396" y2="18" stroke="var(--ink)" stroke-width="4"/>
    </svg>
    <p class="title title--joiner">of</p>
    <p class="title title--bottom">Lanterns</p>

    <div class="knot-frame" role="img" aria-label="Gold Celtic knotwork framing the emblem"></div>

    <div class="emblem" role="img" aria-label="Night sky illustration with a dragon-shaped comet above a mountain range"></div>
    <p class="emblem__caption">White Wine</p>

    <p class="spec spec--abv">14 %</p>
    <p class="spec spec--volume">0.7l</p>
  </main>
</body>
</html>
```